4th Generation Family Business Needs a New Card Design!

We are a family owned 4th Generation company. We are based in the Sydney, Australia area and we are desperately in need of a more modern and classy card. We are monumental masons who design, supply & erect lasting memorials throughout cemeteries in Sydney. Our customers are normally in a period of grieving. I have attached logo files that will need to be implemented on the card. Company was established 1935. Australian Owned and Operated. Card needs to be designed to PRINTLY.com specification.

Target Market(s)

Our target market is based upon people that a grieving for family members that have passed away. We also deal with alot of companies that own and operate cemeteries.

Industry/Entity Type

Business

Contact Information for Business Card

Gavin Pelham, Operations Manager, 0491726053, gavin@pelhamstoneworks.com.au
Brian Pelham, Director, 0417639285, brian@pelhamstoneworks.com.au
Phone # 02 9563 4820
Website: www.pelhamstoneworks.com.au
Address: Suite 17, 9 Lambert Lane, Kellyville, Sydney NSW 2155

Font styles to use
Serif
Decorative
Script

Requirements
Must have
• Would like to see the logo nicely implemented with a modern design. Embossed lettering would be a nice additive.

```html
<!DOCTYPE html>
<html lang="en">
<head>
<meta charset="utf-8">
<title>Pelham Stoneworks — Business Card</title>
<link rel="stylesheet" href="https://fonts.googleapis.com/css2?family=Cinzel:wght@400&family=Arimo:wght@400;700&display=swap">
<style>
  :root {
    --bg: #e9e6e1;
    --card-white: #ffffff;
    --card-black: #1c1c1c;
    --ink: #2b2b2b;
    --ink-soft: #555555;
    --gold: #e8bd2c;
    --rule: #d9d9d9;
    --white: #ffffff;
  }
  * { box-sizing: border-box; margin: 0; padding: 0; }
  html, body { width: 1200px; height: 950px; overflow: hidden; }
  body {
    background: var(--bg);
    font-family: "Arimo", Arial, sans-serif;
    color: var(--ink);
    position: relative;
  }
  .card {
    position: absolute;
    left: 260px;
    width: 680px;
    height: 416px;
    overflow: hidden;
    box-shadow: 0 6px 18px rgba(0,0,0,0.18);
  }
  .card-front { top: 40px; background: var(--card-white); }
  .card-back  { top: 494px; background: var(--card-black); }

  /* front */
  .front-edge {
    position: absolute; left: 0; right: 0; bottom: 0; height: 16px;
    display: flex;
  }
  .front-edge .gold { background: var(--gold); flex: 1; }
  .front-edge .dark { background: var(--card-black); flex: 2; }

  .brand {
    position: absolute;
    display: flex; flex-direction: column; align-items: center;
  }
  .brand-mark { width: 70px; height: 70px; border: 3px solid currentColor; margin-bottom: 18px; }
  .brand-name {
    font-family: "Cinzel", Georgia, serif;
    font-weight: 400;
    letter-spacing: 4px;
    text-align: center;
    line-height: 1.15;
  }
  .brand-rule { width: 220px; height: 2px; background: var(--gold); margin-top: 14px; }

  .card-front .brand { left: 30px; top: 88px; width: 300px; color: var(--ink); }
  .card-front .brand-name { font-size: 34px; }

  .divider {
    position: absolute; left: 350px; top: 70px; width: 1px; height: 250px;
    background: var(--rule);
  }
  .details { position: absolute; left: 382px; top: 74px; width: 280px; }
  .person-name { font-size: 22px; font-weight: 700; color: var(--ink); }
  .person-title { font-size: 16px; color: var(--gold); margin-top: 4px; }
  .address { font-size: 14px; color: var(--ink-soft); margin-top: 12px; line-height: 1.5; }
  .contact-list { list-style: none; margin-top: 22px; border-top: 1px solid var(--rule); padding-top: 14px; }
  .contact-list li {
    display: flex; align-items: center; gap: 10px;
    font-size: 14px; color: var(--ink-soft); line-height: 1.9;
  }
  .contact-list svg { width: 15px; height: 15px; flex: none; fill: var(--ink); }

  /* back */
  .card-back .brand { left: 0; right: 0; top: 110px; color: var(--white); }
  .card-back .brand-name { font-size: 40px; }
</style>
</head>
<body>

<section class="card card-front" aria-label="Business card front">
  <div class="brand">
    <span class="brand-mark"></span>
    <div class="brand-name">PELHAM<br>STONEWORKS</div>
    <span class="brand-rule"></span>
  </div>

  <span class="divider"></span>

  <div class="details">
    <div class="person-name">Gavin Pelham</div>
    <div class="person-title">Operations Manager</div>
    <div class="address">Suite 17, 9 Lambert Lane<br>Kellyville, Sydney NSW 2155</div>
    <ul class="contact-list">
      <li>
        <svg viewBox="0 0 16 16"><path d="M3 1h3l1.5 4-2 1.3a9 9 0 0 0 4.2 4.2L11 8.5l4 1.5v3a2 2 0 0 1-2 2A12 12 0 0 1 1 3a2 2 0 0 1 2-2z"/></svg>
        02 9563 4820
      </li>
      <li>
        <svg viewBox="0 0 16 16"><path d="M4 0h8a1 1 0 0 1 1 1v14a1 1 0 0 1-1 1H4a1 1 0 0 1-1-1V1a1 1 0 0 1 1-1zm1 2v10h6V2zm3 11a1 1 0 1 0 0 2 1 1 0 0 0 0-2z"/></svg>
        0491726053
      </li>
      <li>
        <svg viewBox="0 0 16 16"><path d="M1 3h14v10H1zm1.5 1.2V12h11V4.2L8 8.5z"/><path d="M2 3h12L8 7.5z"/></svg>
        gavin@pelhamstoneworks.com.au
      </li>
      <li>
        <svg viewBox="0 0 16 16"><path d="M8 0a8 8 0 1 0 0 16A8 8 0 0 0 8 0zm0 2a6 6 0 0 1 5.7 4H10.9A11 11 0 0 0 9.4 2.2 6 6 0 0 1 8 2zM2.3 6A6 6 0 0 1 6.6 2.2 11 11 0 0 0 5.1 6zm0 4h2.8a11 11 0 0 0 1.5 3.8A6 6 0 0 1 2.3 10zm4.8 0h1.8a9 9 0 0 1-.9 3.2A9 9 0 0 1 7.1 10zm0-4a9 9 0 0 1 .9-3.2A9 9 0 0 1 8.9 6zm3.8 4h2.8a6 6 0 0 1-4.3 3.8A11 11 0 0 0 10.9 10z"/></svg>
        www.pelhamstoneworks.com.au
      </li>
    </ul>
  </div>

  <div class="front-edge"><span class="gold"></span><span class="dark"></span><span class="gold"></span></div>
</section>

<section class="card card-back" aria-label="Business card back">
  <div class="brand">
    <span class="brand-mark"></span>
    <div class="brand-name">PELHAM<br>STONEWORKS</div>
    <span class="brand-rule"></span>
  </div>
</section>

</body>
</html>
```